[Fun Project] Design A Website For A Semi Pro Soccer Team!

DESIGN ONLY! [NO CODING NEEDED]

Hey,

Thanks for looking! Are you ready to design a cool project with us?

This may be a once in a lifetime opportunity to design a website for a Semi Pro Soccer Team. Projects like this don't come along very often! This will be a lot of fun for you!

We need a fresh and exciting website design for a new soccer (or football, depending on where you are) team. You can view the existing site here: http://www.pwxdunefc.com/

You can get a sense of the team colors and whatnot from that, but the layout is a little dull. We need something more like this: http://www.mendelhollow.com.

We need something that is visual and exciting, something that will appeal to a sports fan. Ideally, we'd love to work with a designer is a fan of the game, as we think he/she would design something more appealing to the demographic.

Be sure to follow the link below and check out our video:

http://clipnest.com/user4417032/review/30582714/4c1d7a90fe

Thank you and good luck!

Target Market(s)

Soccer/football fans and those interested in becoming fans. More than likely, we're talking males 18-40, but don't want to rule out females.

Font styles to use
Sans Serif

Colors
faee3e
fbed22
eb1f27
000000
f6f6f6

Requirements
Must have
• Picture/video slider in the top left (see video)
1 home page design and 2 interior page designs
Should not have
• Cluttered
Dull
Lame
Poor Design
And for the love of all the is holy please do not submit us a theme or a template from some website. We are smarter then that and will just remove you from the project....REAL Designers, we got your back and won't even consider crappy stuff....

```html
<!DOCTYPE html>
<html lang="en">
<head>
<meta charset="utf-8">
<title>Pinewick Dune FC</title>
<link rel="stylesheet" href="https://fonts.googleapis.com/css2?family=Arimo:wght@400;700&display=swap">
<style>
:root{
  --black:#000;
  --page:#fff;
  --footer:#1f1e1d;
  --red:#ec2330;
  --accent:#f0a81c;
  --more:#f7c600;
  --air-red:#d2393b;
  --air-blue:#3d8ed4;
  --text:#111;
  --muted:#9a9a9a;
  --card-line:#dcdcdc;
}
*{box-sizing:border-box;margin:0;padding:0}
html,body{width:1200px;height:611px;overflow:hidden;background:var(--black);font-family:"Arimo",Arial,sans-serif}
.page{position:absolute;left:142px;top:0;width:922px;height:357px;background:var(--page)}
.section-label{position:absolute;left:6px;width:28px;border-right:2px solid var(--red);display:flex;align-items:center;justify-content:center}
.section-label span{transform:rotate(-90deg);font-size:25px;letter-spacing:2px;color:var(--text);white-space:nowrap}
.news-label{top:0;height:138px}
.videos-label{top:167px;height:156px}
.card{position:absolute;width:140px;background:#fff;border:1px solid var(--card-line);border-radius:3px;box-shadow:0 4px 4px -2px rgba(0,0,0,.15);padding:3px}
.card .photo{display:block;width:100%;height:79px;border-radius:1px}
.news .card{top:-14px;height:152px}
.videos .card{top:167px;height:156px}
.card h3{font-size:9.5px;font-weight:700;margin:4px 0 2px 2px;color:var(--text)}
.card p{font-size:8.4px;line-height:10.5px;margin-left:2px;color:var(--text)}
.card .more{position:absolute;right:8px;bottom:5px;font-size:8.5px;font-weight:700;color:var(--more)}
.ph-a{background:linear-gradient(135deg,#8a2a3a,#3a4a30 60%,#c8c0a8)}
.ph-b{background:linear-gradient(180deg,#7e8ea8,#3f6e38 60%,#2e3a28)}
.ph-c{background:linear-gradient(120deg,#2a3a5a,#d8d8d0 50%,#4e7a3a)}
.ph-d{background:linear-gradient(160deg,#6a2230,#a84050 50%,#d8c8c0)}
.match-box{position:absolute;left:633px;top:0;width:282px;height:102px;background:var(--red);color:#fff;text-align:center}
.match-cols{display:flex;justify-content:space-around;padding:1px 4px 0}
.match-cols div{width:90px;font-size:12px;line-height:14px}
.match-cols b{display:block;margin-top:16px;font-size:14px}
.tickets{position:absolute;left:108px;top:70px;width:72px;height:23px;border-radius:4px;background:linear-gradient(#555,#000);color:#fff;font-weight:700;font-size:13px;line-height:22px}
.footer{position:absolute;left:142px;top:357px;width:922px;height:254px;background:var(--footer);color:#fff}
.footer h4{font-size:14px;font-weight:700;color:var(--accent);letter-spacing:.5px}
.explore{position:absolute;left:32px;top:22px}
.explore ul{list-style:none;margin-top:8px}
.explore li{font-size:14px;line-height:24px}
.contact{position:absolute;left:247px;top:22px;font-size:14px;line-height:26px}
.contact h4{margin-bottom:4px}
.contact .muted{color:var(--muted)}
.follow{position:absolute;left:249px;top:210px;display:flex;align-items:center;gap:10px}
.follow h4{margin-right:4px}
.social{display:flex;align-items:center;gap:3px;font-size:10px}
.social i{width:9px;height:9px;border-radius:50%;background:var(--accent)}
.newsletter{position:absolute;left:559px;top:24px;width:339px;height:122px;border-radius:4px;padding:7px;
  background:repeating-linear-gradient(135deg,var(--air-red) 0 10px,#fff 10px 15px,var(--air-blue) 15px 25px,#fff 25px 30px)}
.newsletter .inner{position:relative;width:100%;height:100%;background:#ececec;color:#111}
.newsletter h5{position:absolute;left:6px;top:15px;font-size:16px;font-weight:400}
.newsletter .tag{position:absolute;left:14px;top:44px;font-size:9px;line-height:12px;color:#444;padding-right:10px;border-right:1px dashed #bbb;height:58px}
.newsletter label{position:absolute;left:101px;font-size:13px}
.newsletter .field{position:absolute;left:151px;width:159px;height:21px;background:#fff;border:1px solid #ccc;border-radius:3px}
.submit{position:absolute;left:241px;top:73px;width:69px;height:20px;border-radius:4px;border:1px solid #888;background:linear-gradient(#ddd,#aaa);font-size:10px;letter-spacing:1.5px;text-align:center;line-height:18px}
.legal{position:absolute;left:647px;top:163px;font-size:12px;word-spacing:6px}
</style>
</head>
<body>
<main class="page">
  <div class="section-label news-label"><span>NEWS</span></div>
  <section class="news">
    <article class="card" style="left:46px"><div class="photo ph-a" role="img" aria-label="Players in a goalmouth scramble"></div><h3>This is Pixelforge's versn</h3><p>Duis sed odio sit amet nibh vulputate cursus a sit amet mauris. Morbi accumsan ipsum velit.</p><span class="more">MORE</span></article>
    <article class="card" style="left:191px"><div class="photo ph-b" role="img" aria-label="Stadium panorama during a match"></div><h3>This is Pixelforge's versn</h3><p>Duis sed odio sit amet nibh vulputate cursus a sit amet mauris. Morbi accumsan ipsum velit.</p><span class="more">MORE</span></article>
    <article class="card" style="left:337px"><div class="photo ph-c" role="img" aria-label="Goalkeeper making a save"></div><h3>This is Pixelforge's versn</h3><p>Duis sed odio sit amet nibh vulputate cursus a sit amet mauris. Morbi accumsan ipsum velit.</p><span class="more">MORE</span></article>
    <article class="card" style="left:483px"><div class="photo ph-d" role="img" aria-label="Team players celebrating"></div><h3>This is Pixelforge's versn</h3><p>Duis sed odio sit amet nibh vulputate cursus a sit amet mauris. Morbi accumsan ipsum velit.</p><span class="more">MORE</span></article>
  </section>
  <div class="section-label videos-label"><span>VIDEOS</span></div>
  <section class="videos">
    <article class="card" style="left:46px"><div class="photo ph-c" role="img" aria-label="Goalkeeper making a save"></div><h3>This is Pixelforge's versn</h3><p>Duis sed odio sit amet nibh vulputate cursus a sit amet mauris. Morbi accumsan ipsum velit.</p><span class="more">MORE</span></article>
    <article class="card" style="left:191px"><div class="photo ph-d" role="img" aria-label="Team players celebrating"></div><h3>This is Pixelforge's versn</h3><p>Duis sed odio sit amet nibh vulputate cursus a sit amet mauris. Morbi accumsan ipsum velit.</p><span class="more">MORE</span></article>
    <article class="card" style="left:337px"><div class="photo ph-a" role="img" aria-label="Players in a goalmouth scramble"></div><h3>This is Pixelforge's versn</h3><p>Duis sed odio sit amet nibh vulputate cursus a sit amet mauris. Morbi accumsan ipsum velit.</p><span class="more">MORE</span></article>
    <article class="card" style="left:483px"><div class="photo ph-b" role="img" aria-label="Stadium panorama during a match"></div><h3>This is Pixelforge's versn</h3><p>Duis sed odio sit amet nibh vulputate cursus a sit amet mauris. Morbi accumsan ipsum velit.</p><span class="more">MORE</span></article>
  </section>
  <aside class="match-box">
    <div class="match-cols">
      <div>2:00PM MDT<br>at Larkin Field<b>Summit TV</b></div>
      <div>2:00PM MDT<br>at Harrow Field<b>Summit TV</b></div>
      <div>2:00PM MDT<br>at Eastgate Field<b>Summit TV</b></div>
    </div>
    <div class="tickets">Tickets</div>
  </aside>
</main>
<footer class="footer">
  <nav class="explore"><h4>EXPLORE</h4>
    <ul><li>Home</li><li>News</li><li>Stats</li><li>About</li><li>Tickets</li><li>Contact</li><li>Team Shop</li><li>The RDL</li></ul>
  </nav>
  <address class="contact" style="font-style:normal"><h4>CONTACT INFORMATION</h4>
    <div>Pinewick Dune Football Club</div>
    <div class="muted">4172 Corvale Ave NE</div>
    <div class="muted">Suite 208</div>
    <div class="muted">Pinewick, NM</div>
    <div class="muted">87999</div>
    <div>(505) 555-0148</div>
  </address>
  <div class="follow"><h4>FOLLOW US</h4>
    <span class="social"><i></i>Hubly</span>
    <span class="social"><i></i>Chirpo</span>
    <span class="social"><i></i>Reelo</span>
    <span class="social"><i></i>Tackly</span>
  </div>
  <form class="newsletter"><div class="inner">
    <h5>Newsletter</h5>
    <p class="tag">Stay updated<br>with our news.</p>
    <label style="top:18px">Name</label><span class="field" style="top:16px"></span>
    <label style="top:46px">Email</label><span class="field" style="top:44px"></span>
    <span class="submit">SUBMIT</span>
  </div></form>
  <div class="legal">Legal Privacy Policy Sitemap</div>
</footer>
</body>
</html>
```